Home Page Redesign for Pet Website

Looking to redesign the home page of our WORDPRESS website which will be renamed The Animal Cover Handbook 2015.

Looking for clean design which communicates clarity.
Updates

This is for a Wordpress site.

Please note that the design MUST include the content which is shown in the table in the brief!

Hi Thanks for the designs so far. We have just updated the brief to provide more information and clarify a few issues. We have also now included a couple of layout suggestions. They are just suggestions but it should give you a better idea of what we are looking for. And we have just increased the budget for 1st place by £120. Please feel free to message me if you have any questions. Many thanks. Mabel

Please note that the new brief is in a file dated 25 Jan!

Project Deadline Extended
Reason: We have extended the deadline so we can continue working with the designers who have submitted designs we like. If you have any new designs please submit them by the original deadline of 7.37pm this evening (GMT). We are planning to make our final decision by Friday this week.

Target Market(s)

UK pet owners. All ages but largest age group is 35-50.

Industry/Entity Type

Insurance

Requirements
Must have
• Three clear content groups - LEARN, RESEARCH, CAMPAIGN (see brief for more details).
Stock photos with dogs and cats
Use current colour scheme
Must work with existing inner pages.
Existing font.. but 1pt larger
See brief for more details
Should not have
• Logo
Content from Existing Page (except for footer content... and menu headings).

```html
<!DOCTYPE html>
<html lang="en">
<head>
<meta charset="utf-8">
<title>The Animal Cover Handbook 2015</title>
<link href="https://fonts.googleapis.com/css2?family=Open+Sans:wght@300;400;600;700&display=swap" rel="stylesheet">
<style>
:root{
  --blue:#1d74d8;
  --blue-dark:#1a5fa8;
  --orange:#f7892b;
  --text:#3a3a3a;
  --muted:#6b6b6b;
  --light-bg:#f4f4f4;
  --footer:#3d3d3d;
  --footer-bar:#333333;
  --footer-text:#9a9a9a;
  --white:#ffffff;
}
*{margin:0;padding:0;box-sizing:border-box}
html,body{width:1200px;height:2230px;overflow:hidden}
body{font-family:"Open Sans",Arial,sans-serif;color:var(--text);background:var(--white);position:relative}
.section{position:absolute;left:0;width:1200px}

/* header + hero */
.hero{top:0;height:684px;background:linear-gradient(90deg,#f3f3f3 0%,#f7f7f7 45%,#eeeeee 100%)}
.hero-art{position:absolute;left:490px;top:110px;width:710px;height:574px;
  background:radial-gradient(ellipse at 70% 45%,#d9b98a 0%,#cfa873 28%,#e9e4dc 55%,rgba(240,240,240,0) 75%),
             radial-gradient(ellipse at 25% 70%,#444 0%,#9a9a9a 18%,rgba(240,240,240,0) 40%)}
.brand{position:absolute;left:110px;top:14px;width:240px;text-align:center;color:var(--blue-dark);font-weight:600}
.brand-the{display:block;font-size:26px;line-height:28px}
.brand-name{display:block;font-size:22px;line-height:26px;letter-spacing:.3px}
.brand-year{display:block;font-size:20px;line-height:24px;letter-spacing:2px}
.search{position:absolute;left:869px;top:24px;width:221px;height:29px;border:1px solid #9a9a9a;border-radius:2px;background:var(--white);font-size:12px;color:#999;padding:6px 10px}
.search svg{position:absolute;right:7px;top:7px}
.nav{position:absolute;top:78px;left:556px;display:flex;align-items:center;gap:0;list-style:none;font-size:12px;color:#333}
.nav li{margin-right:44px}
.nav li:last-child{margin-right:0}
.nav .active{background:var(--blue-dark);color:var(--white);padding:5px 10px;border-radius:2px}
.hero-title{position:absolute;left:112px;top:278px;font-size:44px;font-weight:400;line-height:50px;color:#333}
.hero-title em{font-style:normal;color:var(--orange);font-weight:600}
.hero-sub{position:absolute;left:112px;top:392px;width:470px;font-size:21px;line-height:26px;color:#9a9a9a;font-weight:400}
.btn{position:absolute;top:474px;height:39px;font-size:13px;display:flex;align-items:center;justify-content:center;border-radius:2px}
.btn-primary{left:112px;width:147px;background:var(--blue);color:var(--white)}
.btn-outline{left:284px;width:157px;border:1px solid #333;color:#222;background:var(--white)}

/* features */
.features{top:684px;height:521px;background:var(--white)}
.section-title{position:absolute;left:0;width:1200px;text-align:center;font-size:36px;font-weight:400;color:#555}
.section-title strong{font-weight:600;color:var(--blue);position:relative}
.section-title strong::after{content:"";position:absolute;left:0;right:0;bottom:-6px;height:3px;background:var(--blue)}
.features .section-title{top:38px}
.feature{position:absolute;top:120px;width:260px;text-align:center}
.feature-icon{width:160px;height:130px;margin:0 auto;border-radius:50%;background:radial-gradient(circle,#e2e2e2 0%,#ececec 55%,rgba(255,255,255,0) 72%)}
.feature h3{margin-top:36px;font-size:25px;font-weight:700;color:#555;line-height:28px}
.feature h4{font-size:14px;font-weight:400;color:#555;line-height:18px}
.feature p{margin-top:14px;font-size:13px;line-height:22px;color:#666}
.feature a{display:block;margin-top:18px;font-size:13px;color:var(--orange);text-decoration:none}

/* resources */
.resources{top:1205px;height:377px;background:var(--light-bg)}
.resources .section-title{top:38px}
.resources-intro{position:absolute;left:112px;top:116px;width:985px;text-align:center;font-size:14px;line-height:24px;color:#555}
.partners{position:absolute;left:112px;top:248px;width:985px;display:flex;justify-content:space-between;align-items:center}
.partner{width:170px;text-align:center;font-size:21px;line-height:24px;font-weight:600}
.p1{color:#2f5d3a}.p2{color:#6cb33f}.p3{color:#9c1d2a}.p4{color:#f0a81e}.p5{color:#2b67b2}

/* disclaimer */
.disclaimer{top:1582px;height:251px}
.disclaimer h2{position:absolute;top:42px;width:1200px;text-align:center;font-size:32px;font-weight:700;color:#333}
.disclaimer p{position:absolute;left:160px;top:114px;width:880px;text-align:center;font-size:14px;line-height:24px;color:#444}

/* footer */
.footer{top:1833px;height:342px;background:var(--footer);color:var(--footer-text)}
.footer h5{font-size:23px;font-weight:400;color:var(--white);line-height:28px}
.footer-col{position:absolute;top:40px}
.about{left:119px;width:270px}
.about p{margin-top:26px;font-size:14px;line-height:22px}
.posts{left:480px;width:300px}
.posts h5{display:flex;align-items:center;gap:12px}
.posts h5 .dot{width:10px;height:10px;border-radius:50%;background:var(--white)}
.post{display:flex;gap:10px;margin-top:18px}
.post:first-of-type{margin-top:24px}
.avatar{width:40px;height:40px;background:linear-gradient(#8a5a3a,#c9a27e);flex:none}
.post b{display:block;font-size:12px;line-height:14px;color:#e6e6e6;font-weight:700;width:200px}
.post small{display:block;margin-top:5px;font-size:9px;color:#aaa}
.contact{left:855px;width:260px}
.contact p{font-size:14px;line-height:20px}
.contact p:first-of-type{margin-top:32px}
.contact p+p{margin-top:24px}
.social{display:flex;gap:8px;margin-top:42px}
.social span{width:27px;height:27px;border:2px solid #e6e6e6;border-radius:50%}
.footer-bar{top:2175px;height:55px;background:var(--footer-bar);color:var(--footer-text);font-size:14px}
.footer-bar .copy{position:absolute;left:119px;top:18px}
.footer-bar .links{position:absolute;right:102px;top:18px}
</style>
</head>
<body>

<header class="section hero">
  <div class="hero-art" role="img" aria-label="Photo of a black and white kitten beside a golden puppy holding a stethoscope"></div>
  <div class="brand">
    <span class="brand-the">The</span>
    <span class="brand-name">ANIMAL COVER</span>
    <span class="brand-year">HANDBOOK 2015</span>
  </div>
  <div class="search">Search...
    <svg width="12" height="12" viewBox="0 0 12 12"><circle cx="5" cy="5" r="3.6" fill="none" stroke="#f7892b" stroke-width="1.6"/><line x1="7.6" y1="7.6" x2="11" y2="11" stroke="#f7892b" stroke-width="1.8"/></svg>
  </div>
  <ul class="nav">
    <li class="active">HOME</li><li>REVIEWS</li><li>PROVIDERS</li><li>POLICIES</li><li>SURVEYS</li><li>MORE</li>
  </ul>
  <h1 class="hero-title">Welcome to The <em>ANIMAL<br>COVER</em> Handbook 2015</h1>
  <p class="hero-sub">An independent website to help you find the best insurance for your pet</p>
  <span class="btn btn-primary">LEARN MORE</span>
  <span class="btn btn-outline">CHECKOUT POLICIES</span>
</header>

<section class="section features">
  <h2 class="section-title">Our <strong>CORE</strong> Features</h2>
  <div class="feature" style="left:101px">
    <div class="feature-icon" role="img" aria-label="Illustration of a paw print with a blue speech bubble"></div>
    <h3>LEARN</h3><h4>ABOUT PET INSURANCE</h4>
    <p>Lorem ipsum dolor sit amet, consecte-tur adipiscing elit. Etiam elementum elit id velit pellentesque lacinia. Ves-tibulum eu velit lectus.</p>
    <a href="#">Readmore...</a>
  </div>
  <div class="feature" style="left:469px">
    <div class="feature-icon" role="img" aria-label="Illustration of a paw print with a yellow desk lamp"></div>
    <h3>REASEARCH</h3><h4>UK PET INSURANCE Policies</h4>
    <p>Lorem ipsum dolor sit amet, consecte-tur adipiscing elit. Etiam elementum elit id velit pellentesque lacinia. Ves-tibulum eu velit lectus.</p>
    <a href="#">Readmore...</a>
  </div>
  <div class="feature" style="left:848px">
    <div class="feature-icon" role="img" aria-label="Illustration of a paw print with a red marker pen"></div>
    <h3>CAMPAIGN</h3><h4>FOR FAIRER PET INSURANCE</h4>
    <p>Lorem ipsum dolor sit amet, consecte-tur adipiscing elit. Etiam elementum elit id velit pellentesque lacinia. Ves-tibulum eu velit lectus.</p>
    <a href="#">Readmore...</a>
  </div>
</section>

<section class="section resources">
  <h2 class="section-title"><strong>Popular</strong> Resources</h2>
  <p class="resources-intro">Lorem ipsum dolor sit amet, consectetur adipiscing elit. Etiam elementum elit id velit pellentesque lacinia. Vestibulum eu velit lectus. Suspendisse mattis ac ipsum a pretium. Nulla ultricies lacus et purus condimentum, convallis eleifend mi rhoncus. Aenean scelerisque sodales commodo. Interdum et malesuada fames ac ante ipsum primis in faucibus. Suspendisse purus leo,</p>
  <div class="partners">
    <span class="partner p1">Harrow Lane Insurance</span>
    <span class="partner p2">Brightwell Cover</span>
    <span class="partner p3">The Hound Society Pet Insurance</span>
    <span class="partner p4">Tailsure</span>
    <span class="partner p5">Meadowgate Pet Insurance</span>
  </div>
</section>

<section class="section disclaimer">
  <h2>Disclaimar</h2>
  <p>Please note that pet insurance terms often change. Whilst we will do our best to keep this website up to date you must check with the appropriate insurer before making any decisions. If you find any mistakes on this website please do let us know so we can cor-rect it for the benefit of future visitors. Many thanks!</p>
</section>

<footer class="section footer">
  <div class="footer-col about">
    <h5>About Us</h5>
    <p>Animal Cover Surveys UK was founded by a pet owner, Mabel Thornbury, and the website launched early in 2014. Mabel is passionate about ensuring that pet owners make the right pet insurance choice for their pets.</p>
  </div>
  <div class="footer-col posts">
    <h5><span class="dot"></span>Animal Cover Surveys</h5>
    <div class="post"><div class="avatar" role="img" aria-label="Author portrait"></div><div><b>Phasellus molestie magna non est bibendum non venenatis nisl.</b><small>Posted on May 21st &nbsp;|&nbsp; 32 Comments</small></div></div>
    <div class="post"><div class="avatar" role="img" aria-label="Author portrait"></div><div><b>Nullam in dui mauris. Vivamus hendrerit arcu sed erat molestie.</b><small>Posted on May 21st &nbsp;|&nbsp; 32 Comments</small></div></div>
    <div class="post"><div class="avatar" role="img" aria-label="Author portrait"></div><div><b>Mauris iaculis porttitor posuere. Praesent id metus massa, ut.</b><small>Posted on May 21st &nbsp;|&nbsp; 32 Comments</small></div></div>
  </div>
  <div class="footer-col contact">
    <h5>Contact Us</h5>
    <p>Larkford</p>
    <p>mabel@animal-cover-surveys.example</p>
    <p>0100 555 210</p>
    <div class="social"><span></span><span></span><span></span><span></span></div>
  </div>
</footer>

<div class="section footer-bar">
  <span class="copy">© 2015. Animal Cover Surveys UK. All Right Reserved.</span>
  <span class="links">Legal Information &amp; Disclaimers &nbsp;&nbsp;|&nbsp;&nbsp; Privacy Policy</span>
</div>

</body>
</html>
```